BRCW Business Cards

Business Cards should contain:
Bright Ridgeway Coating Works
Colin Pardew
M: 0418 675 913
E: brightRCW@tealmail.example
BRCW logo
TCG logo
Painting & Decorating
Licence # 671392K
slogan: See the Shine of Careful Craftwork

Target Market(s)

all aspect of painting

Industry/Entity Type

Trade

Contact Information for Business Card

Colin Pardew
M: 0418 675 913
E: brightRCW@tealmail.example
BRCW logo
TCG logo
Painting & Decorating
Licence # 671392K

Font styles to use
Serif
Sans Serif

Requirements
Must have
• clear design with nice backround
• two sides
• smal TCG logo
Nice to have
• easy to read
Should not have
• mess
• black
• plastics form

```html
<!DOCTYPE html>
<html lang="en">
<head>
<meta charset="utf-8">
<title>BRCW Business Cards</title>
<link rel="stylesheet" href="https://fonts.googleapis.com/css2?family=Playfair+Display:wght@500&family=Open+Sans:wght@400;700&display=swap">
<style>
  :root {
    --bg: #ececec;
    --green-light: #8fdc8f;
    --green-mid: #5cb85f;
    --green-deep: #3c8a47;
    --teal-dark: #1f5a52;
    --teal-line: #2a9a83;
    --text-green: #2f8a3a;
    --accent-orange: #e8562a;
    --badge-blue: #2c5fa8;
    --paper: #fbfbfb;
    --white: #ffffff;
  }
  * { margin: 0; padding: 0; box-sizing: border-box; }
  html, body { width: 1200px; height: 900px; overflow: hidden; }
  body {
    background: var(--bg);
    font-family: "Open Sans", Arial, sans-serif;
    position: relative;
  }
  .card {
    position: absolute;
    left: 250px;
    width: 700px;
    height: 400px;
    border-radius: 22px;
    overflow: hidden;
    box-shadow: 0 6px 18px rgba(0,0,0,0.15);
  }
  .card-front {
    top: 40px;
    background:
      linear-gradient(125deg, rgba(255,255,255,0.18) 0 38%, transparent 38%),
      linear-gradient(35deg, transparent 0 55%, rgba(255,255,255,0.08) 55%),
      linear-gradient(160deg, var(--green-light) 0%, var(--green-mid) 50%, var(--green-deep) 100%);
  }
  .card-back { top: 460px; background: var(--paper); }

  .brand-lockup {
    position: absolute;
    display: flex;
    align-items: center;
    gap: 18px;
  }
  .brand-dot {
    width: 46px; height: 46px;
    border-radius: 50%;
    background: var(--teal-dark);
    flex: none;
  }
  .brand-divider {
    width: 1px; height: 120px;
    background: var(--teal-dark);
    opacity: 0.6;
  }
  .brand-text { font-family: "Playfair Display", Georgia, serif; font-weight: 500; color: var(--teal-dark); }
  .brand-short { font-size: 64px; line-height: 1; letter-spacing: 2px; }
  .brand-full { font-size: 22px; line-height: 1.25; margin-top: 6px; white-space: nowrap; }
  .brand-full span { display: block; }

  .card-front .brand-lockup { left: 250px; top: 110px; }
  .slogan {
    position: absolute;
    left: 250px; top: 270px;
    width: 360px;
    text-align: center;
    color: var(--white);
    font-size: 16px;
    letter-spacing: 0.5px;
    white-space: nowrap;
  }

  .card-back .brand-lockup { left: 40px; top: 30px; }
  .card-back .brand-divider { height: 100px; }
  .card-back .brand-short { font-size: 52px; }
  .card-back .brand-full { font-size: 19px; }

  .holder-name {
    position: absolute;
    right: 50px; top: 150px;
    color: var(--accent-orange);
    font-size: 24px;
    font-weight: 700;
  }
  .rule-line {
    position: absolute;
    left: 40px; right: 40px; top: 190px;
    height: 1.5px;
    background: var(--teal-line);
  }
  .assoc-badge { position: absolute; right: 50px; top: 208px; }

  .contact-list {
    position: absolute;
    left: 40px; top: 250px;
    list-style: none;
    color: var(--text-green);
    font-size: 19px;
  }
  .contact-list li { display: flex; align-items: center; gap: 14px; margin-bottom: 8px; }
  .contact-icon { width: 22px; height: 22px; flex: none; }
  .trade-line {
    position: absolute;
    left: 40px; top: 345px;
    color: var(--text-green);
    font-size: 19px;
  }
  .trade-sep { color: var(--accent-orange); margin: 0 6px; }
</style>
</head>
<body>
  <section class="card card-front">
    <div class="brand-lockup">
      <span class="brand-dot"></span>
      <span class="brand-divider"></span>
      <div class="brand-text">
        <div class="brand-short">BRCW</div>
        <div class="brand-full"><span>Bright Ridgeway</span><span>Coating Works</span></div>
      </div>
    </div>
    <p class="slogan">• See the Shine of Careful Craftwork •</p>
  </section>

  <section class="card card-back">
    <div class="brand-lockup">
      <span class="brand-dot"></span>
      <span class="brand-divider"></span>
      <div class="brand-text">
        <div class="brand-short">BRCW</div>
        <div class="brand-full"><span>Bright Ridgeway</span><span>Coating Works</span></div>
      </div>
    </div>

    <p class="holder-name">Colin Pardew</p>
    <div class="rule-line"></div>

    <svg class="assoc-badge" width="110" height="70" viewBox="0 0 110 70" role="img" aria-label="TCG association badge">
      <rect x="0" y="0" width="110" height="70" rx="6" fill="var(--badge-blue)" opacity="0.85"/>
    </svg>

    <ul class="contact-list">
      <li>
        <svg class="contact-icon" viewBox="0 0 24 24" aria-hidden="true">
          <circle cx="12" cy="12" r="10.5" fill="none" stroke="var(--accent-orange)" stroke-width="1.8"/>
          <path d="M8.5 7.5c.6-.6 1.3-.5 1.7.1l.9 1.5c.3.5.2 1-.2 1.4l-.6.6c.5 1.2 1.5 2.2 2.7 2.7l.6-.6c.4-.4.9-.5 1.4-.2l1.5.9c.6.4.7 1.1.1 1.7l-.8.8c-.6.6-1.6.7-2.5.3-2.4-1-4.3-2.9-5.3-5.3-.4-.9-.3-1.900.3-2.5z" fill="var(--accent-orange)"/>
        </svg>
        <span>0418 675 913</span>
      </li>
      <li>
        <svg class="contact-icon" viewBox="0 0 24 24" aria-hidden="true">
          <rect x="2" y="5" width="20" height="14" rx="1.5" fill="var(--accent-orange)"/>
          <path d="M3 6l9 7 9-7" fill="none" stroke="var(--white)" stroke-width="1.6"/>
        </svg>
        <span>brightRCW@tealmail.example</span>
      </li>
    </ul>

    <p class="trade-line">Painting &amp; Decorating<span class="trade-sep">//</span>Licence # 671392K</p>
  </section>
</body>
</html>
```